Project Managers Business card design

We need business cards for our Project Managers based in Sydney for our business name Korbet Pty Ltd. We project manage property improvements and infrastructure Assets. We provide asset owners Project Management services from original concept, management of architectural and engineering designs, call and select construction tenders, and manage the Asset operational life cycle to conclusion and removal. We are experienced in feasibility studies, risk assessments, quality control, safety control, environmental analysis. We are specialist in Aged Care and Child Care Services. We can provide asset reviewing checklists, asset inspections, contract cost and contract assessments, dispute resolution services and articles and books on safely working and living in environments subject to analysis. the design colours should be queensland marone and NSW sky blue.

Industry/Entity Type

Construction

Contact Information for Business Card

Gavin Trelowe (Mb 0412 847 391), Dennis Marquay (Mb 0438 216 074), Luke Benhadda,(Mb 0421 963 158)
E: all business cards: korbet@fernmail.example
Office phone number (02) 9482 3165
Address
Level 1 Halyard House
47 Wexford Lane, Parramatta
Web: projectmanagers@worksleadsbykorbet.example (to be checked on Printlyne web draft)

```html
<!DOCTYPE html>
<html lang="en">
<head>
<meta charset="utf-8">
<title>Korbet Pty Ltd – Business Card</title>
<link rel="stylesheet" href="https://fonts.googleapis.com/css2?family=Arimo:wght@400;700&display=swap">
<style>
  :root {
    --stage: #d9d9d9;
    --maroon: #73182c;
    --maroon-deep: #4e0f1e;
    --maroon-night: #2a0911;
    --sky: #7fc8ec;
    --sky-soft: #a9dbf3;
    --paper: #ffffff;
    --card-w: 640px;
    --card-h: 366px;
  }
  * { box-sizing: border-box; margin: 0; padding: 0; }
  html, body {
    width: 1200px;
    height: 945px;
    overflow: hidden;
    background: var(--stage);
    font-family: "Arimo", Arial, sans-serif;
  }
  .canvas { position: relative; width: 1200px; height: 945px; }
  .card {
    position: absolute;
    left: 280px;
    width: var(--card-w);
    height: var(--card-h);
    overflow: hidden;
    box-shadow: 0 6px 18px rgba(0,0,0,0.18);
  }
  .card-front { top: 78px; background: var(--maroon); }
  .card-back  { top: 500px; background: var(--maroon-night); }
  .card-art { position: absolute; inset: 0; width: 100%; height: 100%; }

  .brand {
    position: absolute;
    display: flex;
    align-items: center;
    gap: 12px;
    color: var(--paper);
    font-weight: 700;
    white-space: nowrap;
  }
  .brand-square { background: var(--sky); display: block; }
  .card-front .brand {
    left: 50%; top: 50%;
    transform: translate(-50%, -50%);
    font-size: 46px;
  }
  .card-front .brand-square { width: 30px; height: 30px; }
  .card-back .brand { right: 26px; top: 112px; font-size: 30px; }
  .card-back .brand-square { width: 20px; height: 20px; }

  .person {
    position: absolute;
    left: 26px; top: 34px;
    width: 260px;
    color: var(--paper);
  }
  .person-name {
    font-size: 25px;
    padding-bottom: 5px;
    border-bottom: 1.5px solid var(--sky);
  }
  .person-mobile { font-size: 23px; margin-top: 5px; }

  .contact {
    position: absolute;
    display: flex;
    align-items: center;
    gap: 14px;
    color: var(--paper);
    white-space: nowrap;
  }
  .contact-icon {
    width: 30px; height: 30px;
    background: var(--paper);
    border-radius: 5px;
    display: flex; align-items: center; justify-content: center;
    flex: none;
  }
  .contact-icon svg { width: 18px; height: 18px; }
  .contact-phone { left: 24px; top: 142px; font-size: 21px; }
  .contact-email { left: 24px; top: 210px; font-size: 12.5px; line-height: 1.5; }
  .contact-address { left: 24px; top: 293px; font-size: 18px; gap: 10px; }
  .pin-icon { width: 16px; height: 22px; flex: none; }
</style>
</head>
<body>
<main class="canvas">

  <section class="card card-front" aria-label="Card front">
    <svg class="card-art" viewBox="0 0 640 366">
      <defs>
        <radialGradient id="front-map-tone" cx="50%" cy="45%" r="60%">
          <stop offset="0" stop-color="#7fc8ec" stop-opacity="0.35"/>
          <stop offset="1" stop-color="#73182c" stop-opacity="0"/>
        </radialGradient>
      </defs>
      <rect x="60" y="30" width="520" height="290" fill="url(#front-map-tone)"
            role="img" aria-label="Dotted world map in light sky blue"/>
    </svg>
    <div class="brand">
      <span class="brand-square"></span>
      <span class="brand-name">Korbet</span>
    </div>
  </section>

  <section class="card card-back" aria-label="Card back">
    <svg class="card-art" viewBox="0 0 640 366">
      <defs>
        <radialGradient id="back-map-tone" cx="55%" cy="40%" r="55%">
          <stop offset="0" stop-color="#7fc8ec" stop-opacity="0.22"/>
          <stop offset="1" stop-color="#2a0911" stop-opacity="0"/>
        </radialGradient>
      </defs>
      <rect x="240" y="0" width="360" height="300" fill="url(#back-map-tone)"
            role="img" aria-label="Dotted world map in faint sky blue"/>
      <polygon points="0,128 292,128 322,76 640,76 640,336 0,336" fill="#73182c"/>
      <polygon points="300,76 410,76 450,128 410,186 300,186 336,128" fill="#7fc8ec" opacity="0.35"/>
      <polygon points="0,190 430,190 414,204 0,204" fill="#7fc8ec"/>
      <polygon points="0,266 540,266 524,280 0,280" fill="#7fc8ec"/>
      <polygon points="450,190 640,190 640,204 436,204" fill="#4e0f1e"/>
    </svg>

    <div class="person">
      <p class="person-name">Luke Benhadda</p>
      <p class="person-mobile">Mb 0421 963 158</p>
    </div>

    <div class="contact contact-phone">
      <span class="contact-icon">
        <svg viewBox="0 0 24 24"><path fill="#73182c" d="M6.6 10.8a15.1 15.1 0 0 0 6.6 6.6l2.2-2.2a1 1 0 0 1 1-.25 11.4 11.4 0 0 0 3.6.57 1 1 0 0 1 1 1V20a1 1 0 0 1-1 1A17 17 0 0 1 3 4a1 1 0 0 1 1-1h3.5a1 1 0 0 1 1 1c0 1.25.2 2.45.57 3.57a1 1 0 0 1-.25 1z"/></svg>
      </span>
      <span class="contact-text">(02) 9482 3165</span>
    </div>

    <div class="contact contact-email">
      <span class="contact-icon">
        <svg viewBox="0 0 24 24"><rect x="2" y="5" width="20" height="14" fill="#73182c"/><path d="M2 5l10 8 10-8" fill="none" stroke="#ffffff" stroke-width="1.6"/></svg>
      </span>
      <span class="contact-text">korbet@fernmail.example<br>projectmanagers@worksleadsbykorbet.example</span>
    </div>

    <div class="contact contact-address">
      <svg class="pin-icon" viewBox="0 0 16 22"><path fill="#7fc8ec" d="M8 0a8 8 0 0 0-8 8c0 6 8 14 8 14s8-8 8-14a8 8 0 0 0-8-8zm0 11a3 3 0 1 1 0-6 3 3 0 0 1 0 6z"/></svg>
      <span class="contact-text">Level 1 Halyard House 47 Wexford Lane, Parramatta</span>
    </div>

    <div class="brand">
      <span class="brand-square"></span>
      <span class="brand-name">Korbet</span>
    </div>
  </section>

</main>
</body>
</html>
```